Stationery Design Project for Explainer Video Company

We are a company for explainer videos. We are working together with a community consisting of creative people. The plumtiko videos are animated. Please visit our homepage at www.plumtiko.example, we like our Monitor-Logo, so please create a similar stationary to that. you might use the colours and the font (Pacifico or similar)
We need business cards too. We don't need Facsimile
attached is the logo (please don't use chatterbox text)

Target Market(s)

Marketing, SMB

Industry/Entity Type

Business

```html
<!DOCTYPE html>
<html lang="de">
<head>
<meta charset="utf-8">
<title>plumtiko – Geschäftsausstattung</title>
<link href="https://fonts.googleapis.com/css2?family=Satisfy&family=Pacifico&display=swap" rel="stylesheet">
<style>
  :root {
    --backdrop: #808080;
    --paper: #f8f8f8;
    --brand-red: #c8162a;
    --brand-blue: #1ea6d6;
    --blue-light: #3bbfe2;
    --blue-deep: #0c90c6;
    --ink: #6a6a6a;
    --rule-grey: #bdbdbd;
    --ghost: #e6e5e3;
    --script: "Satisfy", "Pacifico", "Segoe Script", "Brush Script MT", "URW Chancery L", "Comic Sans MS", cursive;
  }
  * { margin: 0; padding: 0; box-sizing: border-box; }
  html, body { width: 1200px; height: 834px; overflow: hidden; }
  body {
    background: var(--backdrop);
    font-family: var(--script);
    position: relative;
  }
  .sheet { position: absolute; background: var(--paper); overflow: hidden; }
  .wordmark {
    position: absolute;
    font-family: var(--script);
    color: var(--brand-red);
    line-height: 1;
    white-space: nowrap;
    transform: translateX(-50%);
  }
  .wordmark--white { color: #fff; }
  .ghost-name {
    position: absolute;
    font-family: var(--script);
    color: var(--ghost);
    line-height: 1;
    white-space: nowrap;
  }
  .rule { position: absolute; height: 1px; }
  .rule--blue { background: var(--brand-blue); }
  .rule--grey { background: var(--rule-grey); }
  .contact {
    position: absolute;
    font-family: var(--script);
    font-style: normal;
    color: var(--ink);
    line-height: 1.2;
    white-space: nowrap;
  }

  /* business card front */
  .card-front {
    left: 87px; top: 35px; width: 238px; height: 137px;
    border-radius: 3px;
    background: linear-gradient(180deg, var(--blue-light), var(--blue-deep));
  }
  .card-front .ghost-name { color: rgba(255,255,255,0.14); font-size: 40px; left: 40px; top: 40px; }
  .card-front .web { position: absolute; left: 0; right: 0; top: 84px; text-align: center; color: #fff; font-size: 8px; }

  /* business card back */
  .card-back { left: 361px; top: 33px; width: 238px; height: 137px; border-radius: 4px; }
  .card-back .contact { font-size: 7px; }

  /* compliment slip */
  .slip { left: 22px; top: 204px; width: 584px; height: 291px; }
  .slip .ghost-name { font-size: 44px; left: 392px; top: 110px; }
  .slip .contact { font-size: 9px; }

  /* envelope */
  .envelope { left: 22px; top: 523px; width: 584px; height: 292px; }
  .envelope .flap { position: absolute; left: 0; top: 0; }
  .envelope .ghost-name { font-size: 56px; left: 16px; top: 190px; }

  /* letterhead */
  .letterhead { left: 619px; top: 28px; width: 558px; height: 787px; }
  .letterhead .ghost-name { font-size: 30px; left: 425px; top: 690px; color: #eeeeec; }
  .letterhead .contact { font-size: 10px; }
</style>
</head>
<body>

  <section class="sheet card-front" aria-label="Visitenkarte Vorderseite">
    <span class="ghost-name" aria-hidden="true">plumtiko</span>
    <span class="wordmark wordmark--white" style="left:119px; top:52px; font-size:20px;">plumtiko</span>
    <p class="web">www.plumtiko.example</p>
  </section>

  <section class="sheet card-back" aria-label="Visitenkarte Rückseite">
    <span class="wordmark" style="left:48px; top:18px; font-size:14px;">plumtiko</span>
    <div class="rule rule--blue" style="left:15px; top:66px; width:206px;"></div>
    <address class="contact" style="left:15px; top:80px;">
      Brightwell GmbH &amp; Co KG<br>Lindenweg 4<br>10115 Musterstadt<br>Deutschland
    </address>
    <p class="contact" style="left:118px; top:97px;">
      Telefon: +49 (0000) 12 34 56<br>Jonas.Beispiel@plumtiko.example
    </p>
  </section>

  <section class="sheet slip" aria-label="Kurzbrief">
    <span class="ghost-name" aria-hidden="true">plumtiko</span>
    <span class="wordmark" style="left:76px; top:38px; font-size:22px;">plumtiko</span>
    <div class="rule rule--grey" style="left:26px; top:227px; width:384px;"></div>
    <address class="contact" style="left:26px; top:235px;">
      Brightwell GmbH &amp; Co KG<br>Lindenweg 4<br>10115 Musterstadt<br>Deutschland
    </address>
    <p class="contact" style="left:130px; top:257px;">
      Telefon: +49 (0000) 12 34 56<br>Jonas.Beispiel@plumtiko.example
    </p>
  </section>

  <section class="sheet envelope" aria-label="Briefumschlag">
    <span class="ghost-name" aria-hidden="true">plumtiko</span>
    <svg class="flap" width="584" height="110" viewBox="0 0 584 110" aria-hidden="true">
      <defs>
        <linearGradient id="flapFill" x1="0" y1="0" x2="0" y2="1">
          <stop offset="0" stop-color="#3bbfe2"/>
          <stop offset="1" stop-color="#0c90c6"/>
        </linearGradient>
      </defs>
      <polygon points="0,0 584,0 292,108" fill="url(#flapFill)"/>
    </svg>
    <span class="wordmark wordmark--white" style="left:292px; top:46px; font-size:22px;">plumtiko</span>
  </section>

  <section class="sheet letterhead" aria-label="Briefbogen">
    <span class="ghost-name" aria-hidden="true">plumtiko</span>
    <span class="wordmark" style="left:279px; top:40px; font-size:22px;">plumtiko</span>
    <div class="rule rule--blue" style="left:89px; top:714px; width:312px;"></div>
    <address class="contact" style="left:99px; top:723px;">
      Brightwell GmbH &amp; Co KG<br>Lindenweg 4<br>10115 Musterstadt<br>Deutschland
    </address>
    <p class="contact" style="left:241px; top:723px;">
      Telefon: +49 (0000) 12 34 56<br>Jonas.Beispiel@plumtiko.example
    </p>
  </section>

</body>
</html>
```